Business Card Design Project

I am looking for a classy business card design for a product design consultancy. We specialize in Product Design, Prototyping, and Manufacturing Consulting. Products that we design range from consumer electronics to household products all the way to sporting goods. We are based in Arizona and called "Heron Design Works." We like to have fun and goof off as much as we like to create new products. We are young and energetic so we would like our business cards to reflect that. We already have a logo that we would like to implement into the card design. A plain rectangular business card is boring so feel free to get creative, but please, no avocado shaped cards (it's far too literal). Also feel free to play around with textured card stocks or plastic. The final design that we choose will pay attention to all of the little details. Our cards will need to be 2 sided. We're giving you guys free reign to design as you would like. Please have fun with this, it will reflect in our business card.

Thanks guys,
Heron Design Works Team

Industry/Entity Type

Electronics

Requirements
Must have
• We would like to have a spot UV coating somewhere on the business card design if possible.
Nice to have
• Let's see some designs with custom shapes rather than typical rectangular business cards but please no avocado shaped cards, thanks. Also play around with textured card socks.

```html
<!DOCTYPE html>
<html lang="en">
<head>
<meta charset="utf-8">
<title>Heron Design Works – Business Cards</title>
<link rel="stylesheet" href="https://fonts.googleapis.com/css2?family=Arimo:ital,wght@0,400;0,700;1,400&display=swap">
<style>
  :root {
    --lime: #8cc63f;
    --lime-deep: #6fae22;
    --ink: #111111;
    --paper: #ffffff;
    --stage: #e4e4e4;
    --text-dark: #1a1a1a;
  }
  * { box-sizing: border-box; margin: 0; padding: 0; }
  html, body { width: 1200px; height: 900px; overflow: hidden; }
  body {
    background: var(--stage);
    font-family: "Arimo", Arial, sans-serif;
    position: relative;
  }
  .card {
    position: absolute;
    width: 500px;
    height: 286px;
    overflow: hidden;
    box-shadow: 0 10px 24px rgba(0,0,0,0.22);
  }
  .card--front-white { left: 70px;  top: 120px; background: var(--paper); }
  .card--back-black  { left: 630px; top: 120px; background: var(--ink); }
  .card--green-stacked { left: 70px;  top: 494px; background: var(--lime); }
  .card--green-split   { left: 630px; top: 494px; background: var(--lime); }

  .wordmark {
    position: absolute;
    display: flex;
    align-items: center;
    gap: 12px;
  }
  .wordmark__dot {
    width: 30px; height: 30px; border-radius: 50%;
    background: currentColor;
    flex: none;
  }
  .wordmark__name {
    font-size: 30px;
    font-weight: 400;
    letter-spacing: 0.5px;
    white-space: nowrap;
  }

  /* White front */
  .card--front-white .wordmark { left: 56px; top: 112px; color: var(--lime-deep); }
  .edge-band {
    position: absolute; right: 0; top: 0; width: 54px; height: 100%;
    background: linear-gradient(90deg, var(--lime) 0%, var(--lime-deep) 100%);
    border-radius: 40px 0 0 40px;
  }
  .url-pill {
    position: absolute; left: 150px; right: 0; bottom: 18px; height: 34px;
    background: var(--lime);
    border-radius: 17px 0 0 17px;
    color: var(--paper);
    font-size: 16px; font-weight: 700;
    display: flex; align-items: center; padding-left: 36px;
  }

  /* Black back */
  .swirl-art {
    position: absolute; inset: 0;
    background:
      radial-gradient(ellipse 60% 40% at 30% 80%, rgba(120,190,50,0.35), transparent 70%),
      radial-gradient(ellipse 45% 35% at 75% 30%, rgba(120,190,50,0.25), transparent 70%),
      var(--ink);
  }
  .card--back-black .wordmark { left: 96px; top: 126px; color: var(--lime); }

  /* Green cards shared */
  .services-band {
    position: absolute; left: 0; right: 0; height: 48px;
    background: var(--ink);
    color: var(--paper);
    text-align: center;
  }
  .services-band__lead {
    display: block; font-size: 10px; font-style: italic; padding-top: 5px;
  }
  .services-band__list {
    display: block; font-size: 15px; margin-top: 3px; word-spacing: 2px;
  }
  .contact {
    position: absolute;
    color: var(--text-dark);
    font-size: 13px;
    line-height: 18px;
    list-style: none;
  }
  .contact__label { color: var(--paper); }

  /* Green stacked */
  .card--green-stacked .wordmark { left: 0; right: 0; top: 26px; justify-content: center; color: var(--paper); }
  .card--green-stacked .services-band { top: 118px; }
  .card--green-stacked .contact { left: 14px; top: 182px; }

  /* Green split */
  .card--green-split .wordmark { left: 14px; top: 78px; color: var(--paper); }
  .card--green-split .wordmark__name { font-size: 22px; }
  .card--green-split .wordmark__dot { width: 22px; height: 22px; gap: 8px; }
  .divider {
    position: absolute; left: 262px; top: 56px; width: 1px; height: 84px;
    background: rgba(0,0,0,0.35);
  }
  .card--green-split .contact { left: 276px; top: 62px; }
  .card--green-split .services-band { bottom: 0; height: 52px; }
</style>
</head>
<body>
  <section class="card card--front-white" aria-label="Card front">
    <div class="edge-band"></div>
    <div class="wordmark"><span class="wordmark__dot"></span><span class="wordmark__name">Heron Design Works</span></div>
    <div class="url-pill">www.herondw.com</div>
  </section>

  <section class="card card--back-black" aria-label="Card back">
    <div class="swirl-art" role="img" aria-label="Glowing green swirl artwork on black"></div>
    <div class="wordmark"><span class="wordmark__dot"></span><span class="wordmark__name">Heron Design Works</span></div>
  </section>

  <section class="card card--green-stacked" aria-label="Green card, stacked layout">
    <div class="wordmark"><span class="wordmark__dot"></span><span class="wordmark__name">Heron Design Works</span></div>
    <div class="services-band">
      <span class="services-band__lead">We specialize in</span>
      <span class="services-band__list">Product Design &nbsp;|&nbsp; Prototyping &nbsp;|&nbsp; Manufacturing Consulting</span>
    </div>
    <ul class="contact">
      <li>#4, Mesa Lane, Tempe - Arizona.</li>
      <li><span class="contact__label">M:</span> 98400 61537</li>
      <li><span class="contact__label">e:</span> info@herondw.com</li>
      <li><span class="contact__label">w:</span> www.herondw.com</li>
    </ul>
  </section>

  <section class="card card--green-split" aria-label="Green card, split layout">
    <div class="wordmark"><span class="wordmark__dot"></span><span class="wordmark__name">Heron Design Works</span></div>
    <div class="divider"></div>
    <ul class="contact">
      <li>#4, Mesa Lane, Tempe - Arizona.</li>
      <li><span class="contact__label">M:</span> 98400 61537</li>
      <li><span class="contact__label">e:</span> info@herondw.com</li>
      <li><span class="contact__label">w:</span> www.herondw.com</li>
    </ul>
    <div class="services-band">
      <span class="services-band__lead">We specialize in</span>
      <span class="services-band__list">Product Design &nbsp;|&nbsp; Prototyping &nbsp;|&nbsp; Manufacturing Consulting</span>
    </div>
  </section>
</body>
</html>
```